Vibrant, yet professional, stationery set and other designs required.

I need to source a fantastic designer for a new project as part of my company using a new logo designed via pixel harbor.

**UPDATE** I am not looking for just 'fine' design that will suffice. I am looking for something great.

We are a life assurance brokerage based in Dublin, Ireland and HearthGuard.ie is our new website aimed at providing services for young families in Ireland. We are hoping to be the 'Vorn' level of service providers in this area and I am looking for the quality of design to reflect this :-) Hopefully that makes sense!

I have a preference for straight lines over curves and waves.

I need...

1. Business card
2. Letterhead
3. Banner (for printing - 76cm X 305cm)
4. Car branding for ZELKA 300 (2014 sport model) I believe the templates are freely available online.

Target Market(s)

Parents in Ireland - Aged 27 to 50.

Industry/Entity Type

Financial Planning

Colors

Designer to choose colors to be used in the design.

Requirements
Must have
• All of the items listed in the description above. I like clean, bright, legible, vibrant and professional design.
Should not have
• No silly or 'cheap' looking designs. This is a professional company looking to provide a professional service.

```html
<!DOCTYPE html>
<html lang="en">
<head>
<meta charset="utf-8">
<title>HearthGuard.ie – Business Card</title>
<link href="https://fonts.googleapis.com/css2?family=Roboto:wght@400;500;700&display=swap" rel="stylesheet">
<style>
  :root {
    --backdrop: #262829;
    --brand-orange: #ef8018;
    --panel-grey: #8e9a9d;
    --card-white: #f2f3f3;
    --logo-grey: #89959a;
    --accent-blue: #5bc3e3;
    --accent-green: #8dc03f;
    --text-white: #ffffff;
  }
  html, body {
    margin: 0;
    padding: 0;
    width: 1200px;
    height: 960px;
    overflow: hidden;
    background: var(--backdrop);
    font-family: "Roboto", Arial, sans-serif;
  }
  .canvas {
    position: relative;
    width: 1200px;
    height: 960px;
  }
  .card {
    position: absolute;
    left: 320px;
    width: 600px;
    height: 342px;
    box-sizing: border-box;
  }

  /* Front */
  .card-front {
    top: 104px;
    background: var(--brand-orange);
    color: var(--text-white);
  }
  .front-brand {
    position: absolute;
    left: 0;
    right: 0;
    top: 138px;
    height: 56px;
    display: flex;
    justify-content: center;
    align-items: center;
    gap: 12px;
  }
  .brand-dot {
    width: 18px;
    height: 18px;
    border-radius: 50%;
    background: var(--text-white);
    flex: none;
  }
  .front-brand .brand-name {
    font-size: 40px;
    font-weight: 700;
    letter-spacing: -0.3px;
    line-height: 1;
    color: var(--text-white);
  }
  .front-url {
    position: absolute;
    left: 0;
    right: 0;
    top: 290px;
    margin: 0;
    text-align: center;
    font-size: 14px;
    line-height: 18px;
    letter-spacing: 6.5px;
  }

  /* Back */
  .card-back {
    top: 493px;
    background: var(--card-white);
    display: flex;
  }
  .contact-panel {
    width: 247px;
    height: 100%;
    background: var(--panel-grey);
    color: var(--text-white);
    box-sizing: border-box;
    padding: 76px 0 0 26px;
    flex: none;
  }
  .contact-name {
    margin: 0;
    font-size: 19px;
    font-weight: 500;
    color: var(--accent-blue);
    text-transform: uppercase;
    line-height: 1.2;
  }
  .contact-role {
    margin: 1px 0 9px;
    font-size: 15px;
    font-weight: 500;
    text-transform: uppercase;
  }
  .contact-address {
    margin: 0 0 9px;
    font-style: normal;
    font-size: 14px;
    line-height: 19px;
  }
  .contact-list {
    list-style: none;
    margin: 0;
    padding: 0;
    font-size: 14px;
    line-height: 19px;
  }
  .contact-list li {
    display: flex;
    align-items: center;
    gap: 9px;
  }
  .contact-list svg {
    width: 13px;
    height: 13px;
    fill: var(--accent-blue);
    flex: none;
  }
  .logo-panel {
    flex: 1;
    position: relative;
    box-sizing: border-box;
    padding-right: 13px;
    display: flex;
    justify-content: center;
    align-items: center;
  }
  .logo-lockup {
    display: flex;
    align-items: center;
    gap: 10px;
    margin-top: 6px;
  }
  .logo-panel .brand-dot {
    width: 16px;
    height: 16px;
    background: var(--brand-orange);
  }
  .logo-panel .brand-name {
    font-size: 34px;
    font-weight: 700;
    letter-spacing: -0.3px;
    line-height: 1;
    color: var(--logo-grey);
  }
  .edge-stripes {
    position: absolute;
    right: 0;
    top: 0;
    bottom: 0;
    width: 13px;
    display: flex;
    flex-direction: column;
    gap: 2px;
    background: var(--card-white);
  }
  .edge-stripes span { flex: 1; }
  .stripe-blue { background: var(--accent-blue); }
  .stripe-orange { background: var(--brand-orange); }
  .stripe-green { background: var(--accent-green); }
</style>
</head>
<body>
<main class="canvas">

  <section class="card card-front" aria-label="Business card front">
    <div class="front-brand">
      <span class="brand-dot"></span>
      <span class="brand-name">HearthGuard.ie</span>
    </div>
    <p class="front-url">www.hearthguard.ie</p>
  </section>

  <section class="card card-back" aria-label="Business card back">
    <div class="contact-panel">
      <h1 class="contact-name">Aidan Brennan</h1>
      <p class="contact-role">CEO/Founder</p>
      <address class="contact-address">14 Larkfield Row<br>Rathmines, Dublin D06 K2R4</address>
      <ul class="contact-list">
        <li>
          <svg viewBox="0 0 16 16" aria-hidden="true"><path d="M3.5 1 6 4 4.6 5.8c.9 2 2.6 3.7 4.6 4.6L11 9l3 2.5-1.5 2.8C7 14 2 9 1.7 3.5Z"/></svg>
          01 482 7715
        </li>
        <li>
          <svg viewBox="0 0 16 16" aria-hidden="true"><path d="M4.5 0h7A1.5 1.5 0 0 1 13 1.5v13a1.5 1.5 0 0 1-1.5 1.5h-7A1.5 1.5 0 0 1 3 14.5v-13A1.5 1.5 0 0 1 4.5 0ZM5 2v10h6V2Zm3 11a1 1 0 1 0 0 2 1 1 0 0 0 0-2Z"/></svg>
          087 316 5042
        </li>
        <li>
          <svg viewBox="0 0 16 16" aria-hidden="true"><path d="M4 1h7v4H4ZM1 6h14v7h-3v2H4v-2H1Zm4 5v3h6v-3Z"/></svg>
          01 482 7716
        </li>
        <li>
          <svg viewBox="0 0 16 16" aria-hidden="true"><path d="M1 3h14v1L8 9 1 4Zm0 2.5 7 5 7-5V13H1Z"/></svg>
          aidan@hearthguard.ie
        </li>
        <li>
          <svg viewBox="0 0 16 16" aria-hidden="true"><circle cx="8" cy="8" r="7"/></svg>
          www.hearthguard.ie
        </li>
      </ul>
    </div>
    <div class="logo-panel">
      <div class="logo-lockup">
        <span class="brand-dot"></span>
        <span class="brand-name">HearthGuard.ie</span>
      </div>
      <div class="edge-stripes" aria-hidden="true">
        <span class="stripe-blue"></span>
        <span class="stripe-orange"></span>
        <span class="stripe-green"></span>
      </div>
    </div>
  </section>

</main>
</body>
</html>
```